Stationery Set for new venture capital firm

We need a new set of stationery including letterhead, business cards, envelopes, with compliment slips for our new startup venture capital firm known as Halvorn.
We make alternative investments globally and hope to have a worldwide network of offices later.

The stationery should be elegant and not too fussy with the use of too many colors.

Venture Capital

```html
<!DOCTYPE html>
<html lang="en">
<head>
<meta charset="utf-8">
<title>Halvorn Stationery Set</title>
<link rel="stylesheet" href="https://fonts.googleapis.com/css2?family=Crimson+Text:wght@400;600&family=Varela+Round&display=swap">
<style>
  :root {
    --blue: #1e9ad6;
    --grey: #7c8084;
    --grey-dark: #6e7276;
    --pale: #e3f0f8;
    --paper: #ffffff;
    --paper-shade: #f1f2f3;
    --ink: #3a3a3a;
    --stage: #e8e5e1;
    --serif: "Crimson Text", Georgia, serif;
    --brand: "Varela Round", Arial, sans-serif;
  }
  * { box-sizing: border-box; margin: 0; padding: 0; }
  html, body { width: 1200px; height: 527px; overflow: hidden; }
  body { background: var(--stage); font-family: var(--serif); color: var(--ink); position: relative; }

  .sheet, .envelope, .card { position: absolute; background: var(--paper); overflow: hidden; box-shadow: 0 1px 3px rgba(0,0,0,.25); }

  .band-top { position: absolute; left: 0; right: 0; top: 0; height: 4px;
    background: linear-gradient(110deg, var(--blue) 0 62%, var(--paper) 62% 63.5%, var(--grey) 63.5%); }
  .band-bottom { position: absolute; left: 0; right: 0; bottom: 0; height: 5px;
    background: linear-gradient(110deg, var(--grey) 0 38%, var(--paper) 38% 39.5%, var(--blue) 39.5%); }

  .brand { position: absolute; display: flex; align-items: center; gap: 5px;
    font-family: var(--brand); color: var(--grey); font-size: 15px; line-height: 1; }
  .brand-dot { width: 14px; height: 14px; border-radius: 50%; background: var(--blue); flex: none; }

  .watermark { position: absolute; border-radius: 50%; background: var(--pale); }

  /* Letterhead */
  .letterhead { left: 20px; top: 23px; width: 344px; height: 445px; }
  .letterhead .brand { left: 15px; top: 38px; }
  .contact-list { position: absolute; right: 12px; top: 20px; border-left: 1px solid #bbb; padding-left: 6px;
    list-style: none; font-size: 6.5px; line-height: 8.6px; }
  .contact-list li { display: flex; align-items: center; gap: 3px; }
  .icon { width: 5px; height: 5px; border-radius: 50%; background: var(--blue); flex: none; display: inline-block; }
  .icon-mail { border-radius: 1px; height: 4px; }
  .letterhead .watermark { left: 5px; top: 270px; width: 200px; height: 200px; }
  .letterhead .address { position: absolute; right: 20px; bottom: 13px; font-size: 7.5px; letter-spacing: .2px; }

  /* Fax sheet */
  .fax { left: 403px; top: 20px; width: 343px; height: 448px;
    background: linear-gradient(160deg, var(--paper) 0%, var(--paper-shade) 100%); }
  .fax .brand { left: 18px; top: 40px; }
  .fax .address { position: absolute; left: 242px; top: 33px; border-left: 1px solid #888; padding-left: 4px;
    font-size: 7.5px; line-height: 8.5px; }
  .fax-title { position: absolute; left: 15px; top: 103px; font-size: 23px; font-weight: 400; letter-spacing: .5px; }
  .fax-fields { position: absolute; left: 15px; top: 146px; width: 293px; display: grid;
    grid-template-columns: 173px 120px; row-gap: 9px; }
  .fax-field { font-size: 6.5px; border-bottom: 1px solid #888; height: 10px; padding-left: 1px; }
  .fax-field + .fax-field:nth-child(even) { padding-left: 0; }
  .fax-options { position: absolute; left: 15px; top: 240px; width: 318px; display: flex; justify-content: space-between;
    list-style: none; font-size: 6.5px; }
  .fax-options li { display: flex; align-items: center; gap: 4px; }
  .checkbox { width: 7px; height: 7px; border: 1px solid #666; background: var(--paper); }
  .fax-footer { position: absolute; left: 0; right: 0; bottom: 14px; display: flex; justify-content: center; gap: 10px;
    list-style: none; font-size: 6px; }
  .fax-footer li { display: flex; align-items: center; gap: 3px; }

  /* Envelopes */
  .envelope-back { left: 799px; top: 23px; width: 383px; height: 173px; }
  .envelope-mid { left: 786px; top: 99px; width: 384px; height: 100px; }
  .flap { position: absolute; left: 0; top: 0; width: 100%; }
  .envelope-back .watermark { left: 166px; top: 14px; width: 52px; height: 52px; background: #9a9ea2; }
  .envelope-mid .watermark { left: 166px; top: 12px; width: 52px; height: 52px; background: #7fc3e8; }
  .envelope-front { left: 761px; top: 185px; width: 384px; height: 173px; }
  .envelope-front .brand { left: 18px; top: 42px; }
  .envelope-front .watermark { left: 250px; top: 12px; width: 160px; height: 160px; }
  .envelope-front .address { position: absolute; left: 11px; top: 143px; font-size: 7.5px; line-height: 10.5px; }

  /* Business cards */
  .card-front { left: 783px; top: 388px; width: 140px; height: 80px; }
  .card-front .band-top, .card-front .band-bottom { height: 3px; }
  .card-front .brand { left: 6px; top: 12px; font-size: 9px; gap: 3px; }
  .card-front .brand-dot { width: 9px; height: 9px; }
  .card-front .watermark { left: 72px; top: 10px; width: 52px; height: 52px; }
  .card-contacts { position: absolute; left: 6px; top: 44px; list-style: none; font-size: 4px; line-height: 5.3px; }
  .card-contacts li { display: flex; align-items: center; gap: 2px; }
  .card-contacts .icon { width: 3px; height: 3px; }
  .card-address { position: absolute; left: 6px; top: 70px; font-size: 4px; }
  .card-person { position: absolute; left: 92px; top: 65px; text-align: center; line-height: 5px; }
  .card-name { font-size: 6px; color: var(--blue); font-weight: 600; }
  .card-title { font-size: 4.5px; }
  .card-back { left: 933px; top: 389px; width: 141px; height: 80px; }
  .card-back .watermark { left: 45px; top: 10px; width: 52px; height: 52px; }
  .card-back .brand { left: 0; right: 0; top: 37px; justify-content: center; font-size: 19px; color: var(--grey-dark); }
</style>
</head>
<body>

  <section class="envelope envelope-back" aria-label="Envelope, grey flap">
    <svg class="flap" viewBox="0 0 383 80" height="80" aria-hidden="true">
      <path d="M0 0 H383 V8 Q300 30 215 68 Q191 78 168 68 Q83 30 0 8 Z" fill="var(--grey)"/>
    </svg>
    <div class="watermark" role="img" aria-label="Halvorn brand mark placeholder"></div>
  </section>

  <section class="envelope envelope-mid" aria-label="Envelope, blue flap">
    <svg class="flap" viewBox="0 0 384 80" height="80" aria-hidden="true">
      <path d="M0 0 H384 V8 Q300 32 216 70 Q192 80 168 70 Q84 32 0 8 Z" fill="var(--blue)"/>
    </svg>
    <div class="watermark" role="img" aria-label="Halvorn brand mark placeholder"></div>
  </section>

  <section class="envelope envelope-front" aria-label="Envelope front">
    <div class="band-top"></div>
    <div class="watermark" role="img" aria-label="Faint Halvorn brand mark"></div>
    <div class="brand"><span class="brand-dot"></span>Halvorn</div>
    <p class="address">Street Name, City Name, State Zipcode<br>www.halvorn.com</p>
    <div class="band-bottom"></div>
  </section>

  <section class="sheet letterhead" aria-label="Letterhead">
    <div class="band-top"></div>
    <div class="brand"><span class="brand-dot"></span>Halvorn</div>
    <ul class="contact-list">
      <li><span class="icon"></span>123-456-7890</li>
      <li><span class="icon"></span>123-456-7856</li>
      <li><span class="icon icon-mail"></span>hello@halvorn.com</li>
      <li><span class="icon"></span>www.halvorn.com</li>
    </ul>
    <div class="watermark" role="img" aria-label="Faint Halvorn brand mark"></div>
    <p class="address">Street Name, City Name State Zipcode</p>
    <div class="band-bottom"></div>
  </section>

  <section class="sheet fax" aria-label="Fax cover sheet">
    <div class="band-top"></div>
    <div class="brand"><span class="brand-dot"></span>Halvorn</div>
    <p class="address">Street Name, City Name<br>State Zipcode</p>
    <h1 class="fax-title">FAX</h1>
    <div class="fax-fields">
      <div class="fax-field">To :</div><div class="fax-field">From :</div>
      <div class="fax-field">Fax :</div><div class="fax-field">Pages :</div>
      <div class="fax-field">Phone :</div><div class="fax-field">Date :</div>
      <div class="fax-field">Re :</div><div class="fax-field">CC :</div>
    </div>
    <ul class="fax-options">
      <li><span class="checkbox"></span>Urgent</li>
      <li><span class="checkbox"></span>For Review</li>
      <li><span class="checkbox"></span>Please Comment</li>
      <li><span class="checkbox"></span>Please Reply</li>
      <li><span class="checkbox"></span>Please Recycle</li>
    </ul>
    <ul class="fax-footer">
      <li><span class="icon"></span>123-456-7890</li>
      <li><span class="icon"></span>123-456-7856</li>
      <li><span class="icon icon-mail"></span>hello@halvorn.com</li>
      <li><span class="icon"></span>www.halvorn.com</li>
    </ul>
    <div class="band-bottom"></div>
  </section>

  <section class="card card-front" aria-label="Business card front">
    <div class="band-top"></div>
    <div class="watermark" role="img" aria-label="Faint Halvorn brand mark"></div>
    <div class="brand"><span class="brand-dot"></span>Halvorn</div>
    <ul class="card-contacts">
      <li><span class="icon"></span>123-456-7890</li>
      <li><span class="icon"></span>123-456-7856</li>
      <li><span class="icon"></span>hello@halvorn.com</li>
      <li><span class="icon"></span>www.halvorn.com</li>
    </ul>
    <p class="card-address">Street Name, City Name, State Zipcode</p>
    <div class="card-person"><p class="card-name">Your Name</p><p class="card-title">Title</p></div>
    <div class="band-bottom"></div>
  </section>

  <section class="card card-back" aria-label="Business card back">
    <div class="watermark" role="img" aria-label="Faint Halvorn brand mark"></div>
    <div class="brand">Halvorn</div>
  </section>

</body>
</html>
```